Im open to ideas.. I was thinking on my business cards aswell as my logo. a place for my name. email. phone number and abn..

ive attched a file with my business logo. which i dont love the colours.. i was think a dark background with charcoal letters so something along those colour schumes but im open to ideas..

Business

BRL Constructions

```html
<!DOCTYPE html>
<html lang="en">
<head>
<meta charset="utf-8">
<title>BRL Constructions – Business Card</title>
<link rel="stylesheet" href="https://fonts.googleapis.com/css2?family=Questrial&display=swap">
<style>
  :root {
    --page-bg: #e4e4e2;
    --card-dark: #272727;
    --card-mid: #383837;
    --ornament-light: #9a9a98;
    --ink-light: #f4f4f2;
    --rule: rgba(244, 244, 242, 0.7);
  }
  * { margin: 0; padding: 0; box-sizing: border-box; }
  html, body {
    width: 1200px;
    height: 800px;
    overflow: hidden;
    background: var(--page-bg);
    font-family: "Questrial", sans-serif;
  }
  .canvas {
    position: relative;
    width: 1200px;
    height: 800px;
  }
  .business-card {
    position: absolute;
    left: 100px;
    top: 114px;
    width: 1000px;
    height: 572px;
    border-radius: 30px;
    overflow: hidden;
    color: var(--ink-light);
    box-shadow: 0 10px 30px rgba(0, 0, 0, 0.18);
  }
  .card-surface {
    position: absolute;
    inset: 0;
    background: radial-gradient(ellipse at 40% 45%, var(--card-mid) 0%, var(--card-dark) 75%);
  }
  .ornament-area {
    position: absolute;
    top: 0;
    right: 0;
    width: 420px;
    height: 100%;
    background: linear-gradient(90deg, rgba(154, 154, 152, 0) 0%, rgba(154, 154, 152, 0.35) 45%, rgba(154, 154, 152, 0.55) 100%);
  }
  .brand {
    position: absolute;
    left: 70px;
    top: 96px;
    text-transform: uppercase;
    line-height: 1;
  }
  .brand-name {
    display: block;
    font-size: 92px;
    letter-spacing: 4px;
  }
  .brand-tagline {
    display: block;
    margin-top: 10px;
    font-size: 19px;
    letter-spacing: 14px;
  }
  .contact {
    position: absolute;
    left: 70px;
    top: 262px;
    width: 500px;
  }
  .person-name {
    font-size: 32px;
    letter-spacing: 1px;
    text-transform: uppercase;
  }
  .abn {
    margin-top: 8px;
    font-size: 17px;
    letter-spacing: 1px;
  }
  .divider {
    border: 0;
    border-top: 1.5px solid var(--rule);
    margin: 12px 0 18px;
  }
  .contact-line {
    display: flex;
    align-items: center;
    gap: 12px;
    font-size: 26px;
    letter-spacing: 1px;
    text-transform: uppercase;
    margin-bottom: 16px;
  }
  .contact-icon {
    width: 26px;
    height: 26px;
    flex: none;
  }
  .contact-icon circle { fill: var(--ink-light); }
  .contact-icon .glyph { fill: none; stroke: var(--card-dark); stroke-width: 1.6; stroke-linejoin: round; stroke-linecap: round; }
  .contact-icon .glyph-fill { fill: var(--card-dark); }
  .divider-bottom { margin: 0; }
</style>
</head>
<body>
<div class="canvas">
  <section class="business-card">
    <div class="card-surface" role="img" aria-label="Dark charcoal stone texture background"></div>
    <div class="ornament-area" role="img" aria-label="White curved swoosh ornament on the right edge"></div>

    <div class="brand">
      <span class="brand-name">BRL</span>
      <span class="brand-tagline">Constructions</span>
    </div>

    <div class="contact">
      <p class="person-name">Dane Holloway</p>
      <p class="abn">ABN: 51 309 712 468</p>
      <hr class="divider">
      <p class="contact-line">
        <svg class="contact-icon" viewBox="0 0 26 26" aria-hidden="true">
          <circle cx="13" cy="13" r="13"/>
          <rect class="glyph" x="7" y="9" width="12" height="8" rx="1"/>
          <path class="glyph" d="M7.5,9.5 L13,14 L18.5,9.5"/>
        </svg>
        dane.holloway@brl.com
      </p>
      <p class="contact-line">
        <svg class="contact-icon" viewBox="0 0 26 26" aria-hidden="true">
          <circle cx="13" cy="13" r="13"/>
          <path class="glyph-fill" d="M9.2,7 L11.4,7 L12.2,10.2 L10.8,11.4 Q12,14.2 14.6,15.4 L15.8,14 L19,14.8 L19,17 Q18.6,19 16.6,19 Q11,18.4 7.6,12.6 Q7,9 9.2,7 Z"/>
        </svg>
        202-555-0176
      </p>
      <hr class="divider divider-bottom">
    </div>
  </section>
</div>
</body>
</html>
```